NEW Modern Sleek Business Card for VR Language Startup

Our startup is using VR to lead the next wave of world language education. We need a two-sided business card that introduces the larger organization (Quorvel Language Inc) and our contact info on one side and shows the product, Lumidrasca, on the other side.

Side 1 (contact info)= Quorvel Logo and Contact info (name, title, phone, email)

Side 2 (product)= Lumidrasc logo, text, and website
Text= Culturally Immersive Language Learning Games
Website= www.lumidrasc.example

Target Market(s)

Education, Technology

Contact Information for Business Card

Contact info will be updated upon approval of the design. For now, put this as a placeholder.

Perry Hollins
Founder & CEO
phollins@mailtrove.example
(555)-014-2736

Font styles to use
Other font styles liked:
• Gibson and Century Gothic are the brand fonts

Requirements
Nice to have
• I would love to see cohesion between the design and colors of the two logos. I have attached a few business card designs that I like, so you can get a feel for my preferred style.

```html
<!DOCTYPE html>
<html lang="en">
<head>
<meta charset="utf-8">
<title>Quorvel Language — Business Card</title>
<link rel="stylesheet" href="https://fonts.googleapis.com/css2?family=Questrial&display=swap">
<style>
  :root {
    --stage: #2b2b2d;
    --card-dark: #0b0b0c;
    --card-light: #ffffff;
    --ink: #151515;
    --cyan: #35c6d9;
    --brand-blue: #4f86de;
    --violet: #5b5fc7;
    --orange: #f28a3a;
  }
  * { box-sizing: border-box; margin: 0; padding: 0; }
  html, body { width: 1200px; height: 900px; overflow: hidden; }
  body {
    background: var(--stage);
    font-family: "Questrial", sans-serif;
    position: relative;
  }
  .card {
    position: absolute;
    left: 250px;
    width: 700px;
    height: 400px;
    overflow: hidden;
    box-shadow: 0 14px 30px rgba(0,0,0,.45);
  }
  .card--product { top: 30px; background: var(--card-dark); }
  .card--contact { top: 470px; background: var(--card-light); }
  .card svg.layer { position: absolute; inset: 0; }

  /* Product side */
  .product-mark {
    position: absolute; top: 92px; left: 0; right: 0;
    display: flex; justify-content: center; align-items: center; gap: 18px;
  }
  .product-mark__dot {
    width: 44px; height: 44px; border-radius: 50%;
    background: var(--brand-blue);
  }
  .product-mark__name {
    font-size: 58px; color: var(--brand-blue); letter-spacing: 1px; white-space: nowrap;
  }
  .product-tagline {
    position: absolute; top: 196px; left: 0; right: 0;
    text-align: center; color: var(--cyan); font-size: 24px; letter-spacing: .5px;
    white-space: nowrap;
  }
  .product-url {
    position: absolute; top: 292px; left: 0; right: 0;
    text-align: center; color: #f2f2f2; font-size: 19px; letter-spacing: 1px;
  }

  /* Contact side */
  .brand-panel {
    position: absolute; top: 0; left: 0; width: 230px; height: 400px;
    background: linear-gradient(180deg, #f28a3a 0%, #e27f4a 45%, #5a63c4 100%);
  }
  .company-mark {
    position: absolute; top: 142px; right: 22px;
    display: flex; align-items: center; gap: 14px; white-space: nowrap;
  }
  .company-mark__dot {
    width: 36px; height: 36px; border-radius: 50%; background: var(--violet);
  }
  .company-mark__name {
    font-size: 32px; color: var(--ink); letter-spacing: 1px;
  }
  .contact-line {
    position: absolute; right: 22px; display: flex; align-items: center; gap: 10px;
    color: var(--ink); font-size: 21px; white-space: nowrap;
  }
  .contact-line--phone { top: 218px; }
  .contact-line--email { top: 254px; }
  .contact-icon { width: 24px; height: 24px; }
  .person {
    position: absolute; left: 262px; top: 318px; white-space: nowrap;
  }
  .person__name {
    font-size: 31px; color: var(--ink); letter-spacing: .5px;
    -webkit-text-stroke: .6px var(--ink);
  }
  .person__title { font-size: 23px; letter-spacing: .5px; }
  .person__title .role-a { color: var(--cyan); }
  .person__title .role-b { color: var(--orange); }
</style>
</head>
<body>

<section class="card card--product" aria-label="Product side">
  <svg class="layer" width="700" height="400" viewBox="0 0 700 400" aria-hidden="true">
    <line x1="0" y1="262" x2="700" y2="262" stroke="var(--cyan)" stroke-width="1.2"/>
    <line x1="200" y1="340" x2="500" y2="340" stroke="var(--cyan)" stroke-width="1"/>
  </svg>
  <div class="product-mark">
    <span class="product-mark__dot"></span>
    <span class="product-mark__name">Lumidrasc</span>
  </div>
  <p class="product-tagline">Culturally Immersive Language Learning Games</p>
  <p class="product-url">www.lumidrasc.example</p>
</section>

<section class="card card--contact" aria-label="Contact side">
  <div class="brand-panel" role="img" aria-label="Large brand illustration area in orange to violet"></div>
  <svg class="layer" width="700" height="400" viewBox="0 0 700 400" aria-hidden="true">
    <line x1="360" y1="200" x2="680" y2="200" stroke="var(--ink)" stroke-width="1.2"/>
    <line x1="262" y1="306" x2="470" y2="306" stroke="var(--violet)" stroke-width="1.4"/>
    <line x1="470" y1="306" x2="680" y2="306" stroke="var(--ink)" stroke-width="1.2"/>
  </svg>

  <div class="company-mark">
    <span class="company-mark__dot"></span>
    <span class="company-mark__name">Quorvel Language</span>
  </div>

  <p class="contact-line contact-line--phone">
    (555)-014-2736
    <svg class="contact-icon" viewBox="0 0 24 24" aria-hidden="true">
      <circle cx="12" cy="12" r="10.5" fill="none" stroke="var(--orange)" stroke-width="2"/>
      <path d="M8.5 7.5 l2 2 -1 1.4 c.8 1.6 2 2.8 3.6 3.6 l1.4-1 2 2 -1.2 1.3 c-3.6-.4-7.7-4.5-8.1-8.1z" fill="var(--violet)"/>
    </svg>
  </p>
  <p class="contact-line contact-line--email">
    phollins@mailtrove.example
    <svg class="contact-icon" viewBox="0 0 24 24" aria-hidden="true">
      <circle cx="12" cy="12" r="10.5" fill="none" stroke="var(--orange)" stroke-width="2"/>
      <rect x="6.5" y="8" width="11" height="8" rx="1" fill="none" stroke="var(--violet)" stroke-width="1.6"/>
      <path d="M6.8 8.5 L12 12.5 L17.2 8.5" fill="none" stroke="var(--violet)" stroke-width="1.6"/>
    </svg>
  </p>

  <div class="person">
    <p class="person__name">PERRY HOLLINS</p>
    <p class="person__title"><span class="role-a">CEO/</span><span class="role-b">FOUNDER</span></p>
  </div>
</section>

</body>
</html>
```